Create a premium soap bar box bar design for an all-natural, men's skincare brand.

We are launching a men’s premium, natural soap bar and skincare business. To start, we will be launching cold-press, all-natural soap bars with a few additional products such as lotions. We plan to expand our line into additional skincare products such as face exfoliants, moisturizers and cleansers that target basic needs such as anti-aging, clarifying and hydrating.

Our target audience is men ages 25-50, with a secondary audience of male teens. Our target audience are mid to high income, professionals that live in more urban areas, but enjoy being active outdoors after work and on the weekends. Our target audience are hard workers, humble and want to enjoy all that life has to offer – whether that’s on top of a mountain or an ocean wave. They hike, bike, skateboard, surf or any other sport that gets them outside. They are husbands, brothers and fathers – there for their family and friends.

Our brand is sophisticated, adventurous and has a sense of humor. Many of our competitors either focus on the rugged outdoors or are more pretentious. We are in-between. We are free spirited and love the fresh air. Our products are trustworthy with no toxic chemicals or harsh ingredients. We are all-natural and provide high-quality, premium products that our audience expects and deserves.

Target Market(s)

Men, ages 25-54 who are high-earning professionals, yet enjoy getting outdoors and being active on the weekends - hiking, biking, surfing, skateboarding and more.

Industry/Entity Type

Men's skincare

Font styles to use
Sans Serif

Requirements
Must have
• See attachments
Nice to have
• We would prefer to a have a premium, slightly more modern looking design that will appeal to our target audience and slightly higher price point.
Should not have
• Please do not include an icon for the fragrance, i.e. cinnamon sticks. However, we do need some differentiation for the fragrance, i.e. color, etc. as it will be on the shelf with other fragrances.

```html
<!DOCTYPE html>
<html lang="en">
<head>
<meta charset="utf-8">
<title>Ridge Hale – Men's Natural Soap Box Panels</title>
<link rel="stylesheet" href="https://fonts.googleapis.com/css2?family=League+Spartan:wght@400;500;600;700&display=swap">
<style>
  :root {
    --navy: #1b2b43;
    --coral: #e8473f;
    --white: #ffffff;
    --backdrop: #ececec;
    --ink: #1b2b43;
  }
  * { box-sizing: border-box; margin: 0; padding: 0; }
  html, body {
    width: 1179px; height: 1200px; overflow: hidden;
    background: var(--backdrop);
    font-family: "League Spartan", "Helvetica Neue", Arial, sans-serif;
    color: var(--ink);
  }
  .stage {
    position: relative; width: 1179px; height: 1200px;
    display: flex; align-items: center; justify-content: center; gap: 40px;
  }
  .panel {
    position: relative; width: 540px; height: 477px;
    background: var(--white); overflow: hidden;
    box-shadow: 0 10px 28px rgba(0,0,0,.18);
  }

  /* brand name */
  .brand-name {
    position: absolute; font-size: 34px; font-weight: 500;
    letter-spacing: 1px; line-height: 1; color: var(--navy); white-space: nowrap;
  }

  /* front */
  .front-frame-top { position: absolute; left: 25px; top: 43px; width: 200px; height: 7px; background: var(--navy); }
  .front-frame-side { position: absolute; left: 25px; top: 43px; width: 7px; height: 300px; background: var(--navy); }
  .front .brand-name { right: 42px; top: 46px; }
  .product-title {
    position: absolute; left: 76px; top: 128px;
    font-size: 56px; font-weight: 700; line-height: 58px;
    color: var(--navy); letter-spacing: -0.5px;
  }
  .landscape-art {
    position: absolute; left: 0; top: 300px; width: 540px; height: 177px;
    background: linear-gradient(160deg, #f4c7c3 0%, var(--coral) 45%, var(--navy) 75%);
  }
  .net-weight {
    position: absolute; right: 50px; bottom: 22px;
    font-size: 23px; font-weight: 600; color: var(--white); letter-spacing: .5px;
  }

  /* back */
  .back-frame {
    position: absolute; left: 29px; top: 43px; width: 476px; height: 393px;
    border: 7px solid var(--navy);
  }
  .back .brand-name { left: 0; right: 0; text-align: center; top: 76px; }

  .story { position: absolute; left: 53px; top: 135px; width: 236px; }
  .story h2 { font-size: 12.5px; font-weight: 700; color: var(--navy); line-height: 14px; }
  .story p {
    font-size: 10.5px; line-height: 14.3px; text-align: justify; font-weight: 500;
    color: var(--navy);
  }
  .story .ingredients-title { margin-top: 14px; }

  .claims { position: absolute; left: 333px; top: 148px; list-style: none; }
  .claim { display: flex; align-items: center; height: 47px; }
  .claim-icon { width: 32px; height: 32px; flex: none; }
  .claim-rule { width: 2px; height: 30px; background: var(--coral); margin: 0 8px 0 10px; }
  .claim-text {
    font-size: 13px; font-weight: 700; line-height: 15px; color: var(--coral);
    text-transform: uppercase;
  }

  .distributor { position: absolute; left: 334px; top: 295px; color: var(--coral); }
  .distributor h3 { font-size: 13.5px; font-weight: 700; }
  .distributor p { font-size: 10px; line-height: 13px; font-weight: 500; }

  .origin-flag {
    position: absolute; left: 52px; top: 348px; width: 74px; height: 48px;
    background: linear-gradient(180deg, #c94a4a, #e9e3e3 50%, #c94a4a);
  }
  .origin-label {
    position: absolute; left: 52px; top: 400px; font-size: 9px; font-weight: 700; color: var(--navy);
  }
  .recycle-mark {
    position: absolute; left: 138px; top: 350px; width: 46px; height: 46px;
    border-radius: 50%; background: var(--navy);
  }
</style>
</head>
<body>
<main class="stage">

  <section class="panel front" aria-label="Front panel">
    <span class="front-frame-top"></span>
    <span class="front-frame-side"></span>
    <span class="brand-name">RIDGE HALE</span>
    <h1 class="product-title">MEN’S<br>NATURAL<br>SOAP</h1>
    <div class="landscape-art" role="img" aria-label="Illustration of pine trees on a navy hill with a coral sweep"></div>
    <p class="net-weight">5 Oz. Bar</p>
  </section>

  <section class="panel back" aria-label="Back panel">
    <div class="back-frame"></div>
    <span class="brand-name">RIDGE HALE</span>

    <div class="story">
      <h2>REAL INGREDIENTS FOR REAL GUYS.</h2>
      <p>Bring the outdoors in using real, natural ingredients on your skin. Traditional bar soap contains harsh chemical ingredients that can be harmful to you and the environment. Lather up with Ridge Hale’s handcrafted, all-natural soap and feel the difference.</p>
      <h2 class="ingredients-title">INGREDIENTS:</h2>
      <p>Ingredients: Vegetable Oil Blend (Olive Oil, Organic Sustainable Palm Oil, Coconut Oil, Shea Butter, Sunflower Oil), Water, Sodium Hydroxide, Beeswax, Cinnamon Essential Oil, Honey, Ground Cinnamon</p>
    </div>

    <ul class="claims">
      <li class="claim">
        <svg class="claim-icon" viewBox="0 0 32 32" aria-hidden="true"><circle cx="16" cy="16" r="14" fill="none" stroke="var(--coral)" stroke-width="2"/><path d="M10 16.5l4 4 8-9" fill="none" stroke="var(--coral)" stroke-width="2"/></svg>
        <span class="claim-rule"></span>
        <span class="claim-text">No harsh<br>chemicals</span>
      </li>
      <li class="claim">
        <svg class="claim-icon" viewBox="0 0 32 32" aria-hidden="true"><circle cx="16" cy="16" r="14" fill="none" stroke="var(--coral)" stroke-width="2"/><path d="M10 16.5l4 4 8-9" fill="none" stroke="var(--coral)" stroke-width="2"/></svg>
        <span class="claim-rule"></span>
        <span class="claim-text">Sustainably<br>sourced</span>
      </li>
      <li class="claim">
        <svg class="claim-icon" viewBox="0 0 32 32" aria-hidden="true"><circle cx="16" cy="16" r="14" fill="none" stroke="var(--coral)" stroke-width="2"/><path d="M10 16.5l4 4 8-9" fill="none" stroke="var(--coral)" stroke-width="2"/></svg>
        <span class="claim-rule"></span>
        <span class="claim-text">Handcrafted</span>
      </li>
    </ul>

    <div class="distributor">
      <h3>Distributed by:</h3>
      <p>Pinecrest Goods Duluth,<br>MN 55802</p>
    </div>

    <div class="origin-flag" role="img" aria-label="United States flag"></div>
    <p class="origin-label">Made in the USA</p>
    <div class="recycle-mark" role="img" aria-label="Recycling symbol"></div>
  </section>

</main>
</body>
</html>
```